I need a cover for a brochure made

I need a cover for a brochure. The dimensions are 8.25 wide and 5.25 high... I also need a .25 inch bleed outside of those dimensions.

I need it to look like a vintage photo album cover. In big words, I would like it to say "Family". Above it in smaller words "To our Harlow Fairway" ... making it look like the words are gold inlay or something.

I would like it kind of in the style of some of the attached maybe. Just vintage looking.

```html
<!DOCTYPE html>
<html lang="en">
<head>
<meta charset="UTF-8">
<title>Family – Brochure Cover</title>
<link href="https://fonts.googleapis.com/css2?family=Great+Vibes&family=Fondamento&display=swap" rel="stylesheet">
<style>
  :root {
    --page-bg: #e5e5e5;
    --leather-light: #4a250b;
    --leather-mid: #2e1706;
    --leather-dark: #0c0502;
    --gold-light: #ffe27a;
    --gold-mid: #f2b82c;
    --gold-deep: #c9860f;
    --gold-shadow: #6b4208;
    --ink: #000000;
  }
  * { margin: 0; padding: 0; box-sizing: border-box; }
  html, body {
    width: 1200px;
    height: 1017px;
    overflow: hidden;
    background: var(--page-bg);
  }
  .cover {
    position: absolute;
    left: 202px;
    top: 255px;
    width: 796px;
    height: 507px;
    overflow: hidden;
    background:
      radial-gradient(ellipse 60% 55% at 48% 40%, var(--leather-light) 0%, var(--leather-mid) 55%, var(--leather-dark) 100%);
  }
  .border-band {
    position: absolute;
    left: 0;
    width: 100%;
    height: 27px;
    background: linear-gradient(180deg, var(--gold-light), var(--gold-mid) 55%, var(--gold-deep));
    opacity: 0.85;
  }
  .border-band--top { top: 0; }
  .border-band--bottom { bottom: 0; }

  .side-ornament {
    position: absolute;
    width: 24px;
    height: 24px;
    background: radial-gradient(circle, var(--gold-light) 0%, var(--gold-mid) 45%, transparent 72%);
  }
  .side-rule {
    position: absolute;
    width: 1px;
    height: 147px;
    top: 183px;
    background: var(--gold-deep);
    opacity: 0.8;
  }

  .dedication {
    position: absolute;
    left: 0;
    width: 100%;
    top: 112px;
    text-align: center;
    font-family: "Great Vibes", cursive;
    font-size: 52px;
    line-height: 80px;
    color: var(--gold-mid);
    background: linear-gradient(180deg, var(--gold-light), var(--gold-mid) 50%, var(--gold-deep));
    -webkit-background-clip: text;
    background-clip: text;
    -webkit-text-fill-color: transparent;
  }
  .title {
    position: absolute;
    left: 0;
    width: 100%;
    top: 222px;
    text-align: center;
    font-family: "Fondamento", serif;
    font-size: 150px;
    line-height: 150px;
    letter-spacing: 1px;
    color: var(--gold-mid);
    filter: drop-shadow(4px 5px 0 var(--ink));
  }
  .title span {
    background: linear-gradient(170deg, var(--gold-light) 0%, var(--gold-mid) 45%, var(--gold-deep) 80%, var(--gold-mid) 100%);
    -webkit-background-clip: text;
    background-clip: text;
    -webkit-text-fill-color: transparent;
  }
</style>
</head>
<body>
  <main class="cover">
    <div class="border-band border-band--top" role="img" aria-label="Gold baroque scroll border"></div>
    <div class="border-band border-band--bottom" role="img" aria-label="Gold baroque scroll border"></div>

    <div class="side-ornament" style="left:26px; top:111px" role="img" aria-label="Small gold flourish"></div>
    <div class="side-ornament" style="left:26px; top:142px" role="img" aria-label="Small gold flourish"></div>
    <div class="side-rule" style="left:38px"></div>
    <div class="side-ornament" style="left:26px; top:344px" role="img" aria-label="Small gold flourish"></div>
    <div class="side-ornament" style="left:26px; top:377px" role="img" aria-label="Small gold flourish"></div>

    <div class="side-ornament" style="left:744px; top:111px" role="img" aria-label="Small gold flourish"></div>
    <div class="side-ornament" style="left:744px; top:142px" role="img" aria-label="Small gold flourish"></div>
    <div class="side-rule" style="left:756px"></div>
    <div class="side-ornament" style="left:744px; top:344px" role="img" aria-label="Small gold flourish"></div>
    <div class="side-ornament" style="left:744px; top:377px" role="img" aria-label="Small gold flourish"></div>

    <p class="dedication">To our Harlow Fairway...</p>
    <h1 class="title"><span>Family</span></h1>
  </main>
</body>
</html>
```